Bref créative
Lark Meadow Stationary
Business Cards, Note Pads, Envelopes, Letterhead etc.
Professional
Doreen Vasquez
Executive Director
2718 North Tolliver Rd. Suite #416
Richardson, Texas 75093
dvasquez@larkmeadow-tx.com
www.larkmeadow-tx.com
Would like to see the card/stationary on cream or ivory colored card stock. Thanks
Lark Meadow Women's Fellowship is the vehicle used to motivate women everywhere to recognize their potential and inner strength through Christ Jesus and use it to propel themselves and others into a new dimension of excellence. Using our talents and resources to build bridges not walls. Yielding a vessel worthy of the title WOMAN.

```html
<!DOCTYPE html>
<html lang="en">
<head>
<meta charset="utf-8">
<title>Lark Meadow Stationary</title>
<link rel="stylesheet" href="https://fonts.googleapis.com/css2?family=Cormorant+Garamond:ital,wght@0,600;1,500&family=Open+Sans:wght@400;700&display=swap">
<style>
:root{
  --backdrop:#6a6a6a;
  --cream:#f8f0c9;
  --ivory:#fbf5da;
  --brown:#5a3415;
  --brown-dark:#3f230c;
  --gold:#c8962e;
  --gold-light:#e3b956;
  --ink:#4a3a2a;
  --faint:#e9dca8;
}
*{box-sizing:border-box;margin:0;padding:0}
html,body{width:1200px;height:758px;overflow:hidden}
body{background:var(--backdrop);position:relative;font-family:"Open Sans",Arial,sans-serif;color:var(--ink)}
.sheet{position:absolute;background:var(--cream);box-shadow:0 3px 8px rgba(0,0,0,.35);overflow:hidden}
.brand{display:flex;align-items:center;gap:5px;font-family:"Cormorant Garamond",Georgia,serif;font-weight:600;color:var(--brown);font-size:12px;white-space:nowrap}
.brand-dot{width:13px;height:13px;border-radius:50%;background:var(--gold);flex:none}
.globe-mark{position:absolute;border-radius:50%;background:radial-gradient(circle,var(--faint) 0%,rgba(233,220,168,.35) 70%,transparent 72%)}

/* business card front */
.card{width:259px;height:154px}
.card-front{left:91px;top:67px}
.card-front .brand{position:absolute;left:14px;top:14px}
.card-name{position:absolute;right:16px;top:16px;text-align:right}
.card-name h1{font-family:"Cormorant Garamond",Georgia,serif;font-weight:600;font-size:17px;color:var(--brown)}
.card-name p{font-size:7px;color:var(--gold);font-weight:700;letter-spacing:.3px}
.card-contact{position:absolute;right:16px;top:62px;text-align:right;font-size:6.3px;line-height:1.55}
.card-wave{position:absolute;left:0;bottom:0}

/* card backs */
.card-back{padding:22px 18px 0;font-size:6.6px;line-height:1.5}
.card-back strong{font-weight:700}
.card-back .card-web{position:absolute;left:0;right:0;bottom:14px;text-align:center;font-size:6.6px;font-weight:700;letter-spacing:.6px}
.back-cream{left:365px;top:67px;background:var(--ivory);color:var(--brown)}
.back-brown{left:629px;top:67px;background:linear-gradient(135deg,var(--brown) 0%,var(--brown-dark) 100%);color:var(--cream)}
.back-gold{left:898px;top:67px;background:linear-gradient(135deg,var(--gold-light) 0%,var(--gold) 60%,#a8741c 100%);color:#fff8e4}

/* notepad */
.notepad{left:91px;top:240px;width:322px;height:187px}
.notepad .brand{position:absolute;left:18px;top:18px}
.notepad .rule{position:absolute;left:42px;top:44px;width:1px;height:120px;background:var(--gold)}

/* envelope */
.envelope{left:91px;top:439px;width:322px;height:257px}
.envelope svg{position:absolute;left:0;top:0}
.envelope .seal{position:absolute;left:0;right:0;top:80px;display:flex;justify-content:center}

/* letterhead & fax shared */
.letterhead{left:444px;top:240px;width:336px;height:456px}
.fax{left:804px;top:240px;width:348px;height:456px}
.doc-head .brand{position:absolute;left:20px;top:20px}
.doc-web{position:absolute;left:20px;top:40px;font-size:5.5px;color:var(--brown);font-weight:700;letter-spacing:.4px}
.doc-address{position:absolute;right:20px;top:20px;text-align:right;font-size:5.5px;line-height:1.55}
.doc-band{position:absolute;left:0;right:0;bottom:0;height:16px;background:var(--brown);border-top:3px solid var(--gold)}
.letter-body{position:absolute;left:44px;right:32px;top:80px;font-size:5.6px;line-height:1.6}
.letter-body p{margin-bottom:8px}
.signature{width:60px;height:16px;margin:4px 0 4px;background:linear-gradient(90deg,rgba(74,58,42,.35),rgba(74,58,42,.1))}

.fax-title{position:absolute;right:22px;top:66px;font-size:16px;letter-spacing:1px;color:var(--brown)}
.fax-table{position:absolute;left:26px;right:22px;top:92px;border-collapse:collapse;font-size:6px}
.fax-table td{border:1px solid #b9a77a;height:15px;padding:0 4px;width:25%}
.fax-table td.label{font-weight:700;color:var(--brown);background:rgba(200,150,46,.12)}
.fax-checks{position:absolute;left:26px;right:22px;top:166px;display:flex;justify-content:space-between;font-size:5.5px}
.fax-checks span{display:flex;align-items:center;gap:3px}
.fax-checks i{width:6px;height:6px;border:1px solid var(--brown);display:inline-block}
.fax-comments{position:absolute;left:26px;top:186px;font-size:6px;font-weight:700;color:var(--brown)}
</style>
</head>
<body>

<!-- business card front -->
<section class="sheet card card-front">
  <div class="brand"><span class="brand-dot"></span>Lark Meadow</div>
  <div class="card-name">
    <h1>Doreen Vasquez</h1>
    <p>Executive Director</p>
  </div>
  <div class="card-contact">
    2718 North Tolliver Rd. Suite #416<br>
    Richardson, Texas 75093<br>
    dvasquez@larkmeadow-tx.com<br>
    www.larkmeadow-tx.com
  </div>
  <svg class="card-wave" width="259" height="70" viewBox="0 0 259 70">
    <path d="M0 30 C60 10 120 70 259 40 L259 70 L0 70Z" fill="var(--gold)"/>
    <path d="M0 42 C70 20 130 78 259 52 L259 70 L0 70Z" fill="var(--brown)"/>
  </svg>
</section>

<!-- card backs -->
<section class="sheet card card-back back-cream">
  <p><strong>Lark Meadow Women's Fellowship</strong> exists to encourage women everywhere to discover their gifts and quiet courage through faith, and to lift one another toward a fuller, kinder way of living. Sharing our time and our means to open doors and welcome every neighbour. Growing hearts that are ready to serve with grace.</p>
  <div class="card-web">www.larkmeadow-tx.com</div>
</section>
<section class="sheet card card-back back-brown">
  <p><strong>Lark Meadow Women's Fellowship</strong> exists to encourage women everywhere to discover their gifts and quiet courage through faith, and to lift one another toward a fuller, kinder way of living. Sharing our time and our means to open doors and welcome every neighbour. Growing hearts that are ready to serve with grace.</p>
  <div class="card-web">www.larkmeadow-tx.com</div>
</section>
<section class="sheet card card-back back-gold">
  <p><strong>Lark Meadow Women's Fellowship</strong> exists to encourage women everywhere to discover their gifts and quiet courage through faith, and to lift one another toward a fuller, kinder way of living. Sharing our time and our means to open doors and welcome every neighbour. Growing hearts that are ready to serve with grace.</p>
  <div class="card-web">www.larkmeadow-tx.com</div>
</section>

<!-- notepad -->
<section class="sheet notepad">
  <div class="brand"><span class="brand-dot"></span>Lark Meadow</div>
  <div class="rule"></div>
  <div class="globe-mark" role="img" aria-label="Faint globe watermark" style="left:210px;top:50px;width:130px;height:130px"></div>
</section>

<!-- envelope -->
<section class="sheet envelope">
  <svg width="322" height="257" viewBox="0 0 322 257">
    <path d="M0 150 L161 112 L322 150 L322 257 L0 257Z" fill="var(--brown)"/>
    <path d="M0 150 L161 112 L322 150" fill="none" stroke="var(--gold)" stroke-width="3"/>
    <path d="M0 0 L161 100 L322 0" fill="none" stroke="#d8c893" stroke-width="1"/>
  </svg>
  <div class="seal"><div class="brand"><span class="brand-dot"></span>Lark Meadow</div></div>
</section>

<!-- letterhead -->
<section class="sheet letterhead">
  <div class="doc-head">
    <div class="brand"><span class="brand-dot"></span>Lark Meadow</div>
    <div class="doc-web">www.larkmeadow-tx.com</div>
    <div class="doc-address">2718 North Tolliver Rd. Suite #416<br>Richardson, Texas 75093<br>dvasquez@larkmeadow-tx.com</div>
  </div>
  <div class="globe-mark" role="img" aria-label="Faint globe watermark" style="left:130px;top:200px;width:170px;height:170px"></div>
  <div class="letter-body">
    <p>Recipient Name<br>100 Main Street<br>Dallas, Texas</p>
    <p>Dear Friend,</p>
    <p>Thank you for your continued support of our fellowship. Your generosity helps women everywhere discover their strength and purpose, and it allows us to keep building bridges in every community we serve.</p>
    <p>This season we will host workshops, mentoring circles and retreats that invite each woman to grow in faith and confidence. We would be honored to have you join us as a partner and friend.</p>
    <p>Please reach out with any questions. We look forward to serving alongside you in the months ahead.</p>
    <p>Warm regards,</p>
    <div class="signature" role="img" aria-label="Handwritten signature"></div>
    <p>Doreen Vasquez<br>Executive Director</p>
  </div>
  <div class="doc-band"></div>
</section>

<!-- fax -->
<section class="sheet fax">
  <div class="doc-head">
    <div class="brand"><span class="brand-dot"></span>Lark Meadow</div>
    <div class="doc-web">www.larkmeadow-tx.com</div>
    <div class="doc-address">2718 North Tolliver Rd. Suite #416<br>Richardson, Texas 75093<br>dvasquez@larkmeadow-tx.com</div>
  </div>
  <div class="fax-title">FAX</div>
  <table class="fax-table">
    <tr><td class="label">To:</td><td></td><td class="label">From:</td><td></td></tr>
    <tr><td class="label">Fax:</td><td></td><td class="label">Pages:</td><td></td></tr>
    <tr><td class="label">Phone:</td><td></td><td class="label">Date:</td><td></td></tr>
    <tr><td class="label">Re:</td><td></td><td class="label">CC:</td><td></td></tr>
  </table>
  <div class="fax-checks">
    <span><i></i>Urgent</span>
    <span><i></i>For Review</span>
    <span><i></i>Please Comment</span>
    <span><i></i>Please Reply</span>
    <span><i></i>Please Recycle</span>
  </div>
  <div class="fax-comments">Comments:</div>
  <div class="globe-mark" role="img" aria-label="Faint globe watermark" style="left:170px;top:230px;width:170px;height:170px"></div>
  <div class="doc-band"></div>
</section>

</body>
</html>
```